Interactive Report Dashboard for Data Analytics

Please see this google doc for information and pictures regarding our project.
https://files.brindlework.net/sheet/d/7XpRmTqWz48NvKdLsEj2HbYf90GcAuUo3iZeMkPn/view?share=open
Feel free to message me if you have any questions.
Target Market(s)
This is for video producers, youtubers, and online teachers.
We run focus groups for them and help them understand how their audience reacts to the video content.
Coding
Coded - Design and coding required
Number of Pages Required
5+ page
Colors
Designer to choose colors to be used in the design.
Look and feel
Each slider illustrates characteristics of the customer's brand and the style your logo design should communicate.

```html
<!DOCTYPE html>
<html lang="en">
<head>
<meta charset="utf-8">
<title>Veranto — Audience Analytic Tools</title>
<link href="https://fonts.googleapis.com/css2?family=Lato:wght@400;700;900&display=swap" rel="stylesheet">
<style>
:root{
  --brand:#1a6bb8;
  --sidebar:#212f86;
  --page:#f2f2f2;
  --card:#ffffff;
  --border:#dcdcdc;
  --accent:#d0111b;
  --text:#333333;
  --muted:#666666;
  --knob:#c9380c;
  --c-blue:#2946c7;
  --c-red:#d42a16;
  --c-orange:#f6910f;
  --c-green:#1d9418;
  --c-purple:#930a9a;
}
*{box-sizing:border-box;margin:0;padding:0}
html,body{width:1200px;height:1124px;overflow:hidden;background:#fff;font-family:'Lato',sans-serif;color:var(--text)}
.topbar{position:absolute;left:0;top:0;width:1200px;height:50px;background:var(--brand);color:#fff}
.brand{position:absolute;left:69px;top:13px;font-size:20px;font-weight:900;letter-spacing:.5px}
.top-actions{position:absolute;right:52px;top:0;height:50px;display:flex;align-items:center;gap:16px;font-size:12.5px}
.top-actions svg{display:block}
.page{position:absolute;left:45px;top:50px;width:1110px;height:1074px;background:var(--page)}
.sidebar{position:absolute;left:53px;top:101px;width:243px;height:1023px;background:var(--sidebar);color:#fff}
.range{position:absolute;left:19px;width:216px}
.range-label{font-size:10px;font-weight:700;letter-spacing:.3px}
.range-track{position:relative;height:4px;background:#fff;margin:9px 8px 0 8px;border-radius:2px}
.range-knob{position:absolute;top:-5px;width:14px;height:14px;border-radius:50%;background:var(--knob);border:2px solid #fff}
.range-values{display:flex;justify-content:space-between;font-size:10.5px;font-weight:700;margin-top:5px}
.filter{position:absolute;left:20px;width:204px;height:34px;background:#fff;color:#333;font-size:12px;padding:0 11px;display:flex;align-items:center;justify-content:space-between}
.copyright{position:absolute;left:13px;top:970px;font-size:10.5px;line-height:18px;font-family:Arial,sans-serif}
.tabs{position:absolute;left:318px;top:62px;width:829px;height:35px;border-bottom:1px solid #d4d4d4}
.tab{position:absolute;top:8px;font-size:11.5px;font-weight:700;color:#333;letter-spacing:.2px}
.tab.active{color:var(--accent)}
.tab-underline{position:absolute;left:0;top:31px;width:172px;height:4px;background:var(--accent)}
.sort{position:absolute;left:559px;top:5px;display:flex;align-items:center;gap:8px;font-size:12px;font-weight:700}
.sort-select{width:118px;height:20px;border:1px solid #ccc;background:#fff;font-size:9.5px;font-weight:400;padding:0 8px;display:flex;align-items:center;justify-content:space-between;color:#555}
.view-icons{position:absolute;right:0;top:7px;display:flex;gap:14px}
.card{position:absolute;width:268px;height:310px;background:var(--card);border:1px solid var(--border)}
.card svg.chart{position:absolute;left:0;top:0;width:268px;height:180px}
.card h2{position:absolute;left:16px;top:168px;font-size:19.5px;font-weight:700;color:var(--brand)}
.card p{position:absolute;left:16px;top:196px;width:240px;font-size:12.5px;line-height:19.5px;color:#444}
.map{position:absolute;left:16px;top:12px;width:236px;height:150px;background:linear-gradient(135deg,#cfe6c4 0%,#6bbd5c 30%,#e4e4e4 55%,#1b8d17 80%,#e8e8e8 100%);border-radius:4px}
svg text{font-family:Arial,sans-serif}
</style>
</head>
<body>
<header class="topbar">
  <div class="brand">VERANTO</div>
  <div class="top-actions">
    <svg width="12" height="13" viewBox="0 0 12 13"><path d="M6 1a4 4 0 0 1 4 4v3l1.5 2h-11L2 8V5a4 4 0 0 1 4-4z M4.5 11h3a1.5 1.5 0 0 1-3 0z" fill="#fff"/></svg>
    <svg width="13" height="13" viewBox="0 0 24 24"><path d="M12 2l3 7h7l-5.5 4.5 2 7.5L12 16.5 5.5 21l2-7.5L2 9h7z" fill="#fff"/></svg>
    <svg width="12" height="12" viewBox="0 0 12 12"><circle cx="6" cy="6" r="6" fill="#fff"/><rect x="5.2" y="5" width="1.6" height="4.5" fill="#1a6bb8"/><circle cx="6" cy="3.3" r="1" fill="#1a6bb8"/></svg>
    <span>User &#8964;</span>
  </div>
</header>

<main class="page"></main>

<aside class="sidebar">
  <div class="range" style="top:9px">
    <div class="range-label">AGE</div>
    <div class="range-track"><span class="range-knob" style="left:-7px"></span><span class="range-knob" style="right:-7px"></span></div>
    <div class="range-values"><span>16.0</span><span>63.0</span></div>
  </div>
  <div class="range" style="top:70px">
    <div class="range-label">INCOME</div>
    <div class="range-track"><span class="range-knob" style="left:-7px"></span><span class="range-knob" style="right:-7px"></span></div>
    <div class="range-values"><span>10,150.0</span><span>119,782.0</span></div>
  </div>
  <div class="filter" style="top:148px">Nationality <span>&#8661;</span></div>
  <div class="filter" style="top:192px">Education <span>&#8661;</span></div>
  <div class="filter" style="top:236px">Gender <span>&#8661;</span></div>
  <div class="filter" style="top:281px">Interest <span>&#8661;</span></div>
  <div class="filter" style="top:326px">Personality <span>&#8661;</span></div>
  <div class="copyright">Copyright © 2018. Company Name.<br>All Right Reserved</div>
</aside>

<nav class="tabs">
  <span class="tab active" style="left:14px">AUDIENCE ANALYTIC TOOLS</span>
  <span class="tab" style="left:193px">REAL TIME EMOTION DISPLAY</span>
  <span class="tab" style="left:381px">SURVEY RESPONSES</span>
  <span class="tab-underline"></span>
  <div class="sort">Sort by: <span class="sort-select">View All <span>&#8661;</span></span></div>
  <div class="view-icons">
    <svg width="12" height="10" viewBox="0 0 12 10" fill="#444"><rect x="0" y="0" width="3" height="2"/><rect x="4.5" y="0" width="3" height="2"/><rect x="9" y="0" width="3" height="2"/><rect x="0" y="4" width="3" height="2"/><rect x="4.5" y="4" width="3" height="2"/><rect x="9" y="4" width="3" height="2"/><rect x="0" y="8" width="3" height="2"/><rect x="4.5" y="8" width="3" height="2"/><rect x="9" y="8" width="3" height="2"/></svg>
    <svg width="12" height="10" viewBox="0 0 12 10" fill="#444"><rect x="0" y="0" width="2.5" height="2"/><rect x="3.5" y="0" width="8.5" height="2"/><rect x="0" y="4" width="2.5" height="2"/><rect x="3.5" y="4" width="8.5" height="2"/><rect x="0" y="8" width="2.5" height="2"/><rect x="3.5" y="8" width="8.5" height="2"/></svg>
    <svg width="11" height="10" viewBox="0 0 11 10" fill="#444"><rect y="1" width="11" height="1"/><rect y="5" width="11" height="1"/><rect y="8.5" width="11" height="1"/><rect x="6" y="0" width="2" height="3"/><rect x="2" y="4" width="2" height="3"/><rect x="7" y="7.5" width="2" height="3"/></svg>
  </div>
</nav>

<!-- Row 1 -->
<article class="card" style="left:319px;top:116px">
  <div class="map" role="img" aria-label="World map shaded green by audience population per country"></div>
  <h2>Geo Chart</h2>
  <p>Lorem ipsum dolor sit amet, consectetur adipiscing elit. Phasellus quis magna turpis. Maecenas varius ornare convallis interdum magna ut augue rutrum luctus placerat gravida sodales..</p>
</article>

<article class="card" style="left:598px;top:116px">
  <svg class="chart" viewBox="0 0 268 180">
    <text x="30" y="16" font-size="5.5" font-weight="bold">Age vs. Weight comparison</text>
    <g stroke="#ddd" stroke-width=".6">
      <line x1="30" y1="25" x2="240" y2="25"/><line x1="30" y1="53" x2="240" y2="53"/><line x1="30" y1="81" x2="240" y2="81"/><line x1="30" y1="109" x2="240" y2="109"/>
      <line x1="82" y1="25" x2="82" y2="137"/><line x1="135" y1="25" x2="135" y2="137"/><line x1="187" y1="25" x2="187" y2="137"/><line x1="240" y1="25" x2="240" y2="137"/>
    </g>
    <line x1="30" y1="137" x2="240" y2="137" stroke="#333" stroke-width=".6"/>
    <g font-size="5" fill="#444" text-anchor="end"><text x="24" y="27">20</text><text x="24" y="55">15</text><text x="24" y="83">10</text><text x="24" y="111">5</text><text x="24" y="139">0</text></g>
    <g font-size="5" fill="#444" text-anchor="middle"><text x="30" y="146">0</text><text x="82" y="146">5</text><text x="135" y="146">10</text><text x="187" y="146">15</text><text x="240" y="146">20</text><text x="135" y="161" font-style="italic">Age</text></g>
    <g fill="#2946c7"><circle cx="61" cy="118" r="1.5"/><circle cx="71" cy="108" r="1.5"/><circle cx="71" cy="110" r="1.5"/><circle cx="98" cy="98" r="1.5"/><circle cx="113" cy="70" r="1.5"/><circle cx="145" cy="59" r="1.5"/></g>
  </svg>
  <h2>Scatter Chart</h2>
  <p>Lorem ipsum dolor sit amet, consectetur adipiscing elit. Phasellus quis magna turpis. Maecenas varius ornare convallis interdum magna ut augue rutrum luctus placerat gravida sodales..</p>
</article>

<article class="card" style="left:878px;top:116px">
  <svg class="chart" viewBox="0 0 268 180">
    <text x="24" y="18" font-size="5.5" font-weight="bold">Lengths of dinosaurs, in meters</text>
    <g stroke="#ddd" stroke-width=".6"><line x1="25" y1="29" x2="254" y2="29"/><line x1="25" y1="59" x2="254" y2="59"/><line x1="25" y1="90" x2="254" y2="90"/><line x1="25" y1="120" x2="254" y2="120"/></g>
    <g fill="#2946c7" stroke="#fff" stroke-width=".4">
      <rect x="25" y="54" width="46" height="97"/><rect x="71" y="127" width="46" height="24"/><rect x="117" y="133" width="46" height="18"/><rect x="163" y="127" width="46" height="24"/><rect x="209" y="145" width="46" height="6"/>
    </g>
    <line x1="25" y1="151" x2="254" y2="151" stroke="#333" stroke-width=".6"/>
    <g font-size="5" fill="#444" text-anchor="end"><text x="20" y="31">20</text><text x="20" y="61">15</text><text x="20" y="92">10</text><text x="20" y="122">5</text><text x="20" y="153">0</text></g>
    <g font-size="5" fill="#444" text-anchor="middle"><text x="25" y="160">0</text><text x="71" y="160">10</text><text x="117" y="160">20</text><text x="163" y="160">30</text><text x="209" y="160">40</text><text x="254" y="160">50</text></g>
  </svg>
  <h2>Histogram</h2>
  <p>Lorem ipsum dolor sit amet, consectetur adipiscing elit. Phasellus quis magna turpis. Maecenas varius ornare convallis interdum magna ut augue rutrum luctus placerat gravida sodales..</p>
</article>

<!-- Row 2 -->
<article class="card" style="left:319px;top:441px">
  <svg class="chart" viewBox="0 0 268 180">
    <text x="68" y="35" font-size="5" font-weight="bold">Population of Largest U.S. Cities</text>
    <g font-size="4.5" fill="#333" text-anchor="end">
      <text x="64" y="53">New York City, NY</text><text x="64" y="68">Los Angeles, CA</text><text x="64" y="83">Chicago, IL</text><text x="64" y="98">Houston, TX</text><text x="64" y="113">Philadelphia, PA</text>
    </g>
    <g stroke="#ddd" stroke-width=".5"><line x1="102" y1="44" x2="102" y2="120"/><line x1="136" y1="44" x2="136" y2="120"/><line x1="170" y1="44" x2="170" y2="120"/><line x1="204" y1="44" x2="204" y2="120"/></g>
    <g fill="#2946c7"><rect x="68" y="47" width="55" height="8"/><rect x="68" y="62" width="26" height="8"/><rect x="68" y="77" width="18" height="8"/><rect x="68" y="92" width="14" height="8"/><rect x="68" y="107" width="10" height="8"/></g>
    <g fill="#d42a16"><rect x="123" y="47" width="54" height="8"/><rect x="94" y="62" width="25" height="8"/><rect x="86" y="77" width="17" height="8"/><rect x="82" y="92" width="12" height="8"/><rect x="78" y="107" width="10" height="8"/></g>
    <line x1="68" y1="44" x2="68" y2="120" stroke="#333" stroke-width=".5"/>
    <g font-size="4.5" fill="#444" text-anchor="middle"><text x="68" y="127">0</text><text x="102" y="127">5,000,000</text><text x="136" y="127">10,000,000</text><text x="170" y="127">15,000,000</text><text x="204" y="127">20,000,000</text><text x="136" y="136" font-style="italic">Total Population</text></g>
    <rect x="209" y="45" width="8" height="3" fill="#2946c7"/><text x="220" y="48" font-size="4.5">2010 Population</text>
    <rect x="209" y="53" width="8" height="3" fill="#d42a16"/><text x="220" y="56" font-size="4.5">2000 Population</text>
  </svg>
  <h2>Bar Charts</h2>
  <p>Lorem ipsum dolor sit amet, consectetur adipiscing elit. Phasellus quis magna turpis. Maecenas varius ornare convallis interdum magna ut augue rutrum luctus placerat gravida sodales..</p>
</article>

<article class="card" style="left:598px;top:441px">
  <svg class="chart" viewBox="0 0 268 180">
    <text x="38" y="21" font-size="5.5" font-weight="bold">My Daily Activities</text>
    <path d="M113 100 L113 37 A63 63 0 0 1 129.4 160.8Z" fill="#2946c7"/>
    <path d="M113 100 L129.4 160.8 A63 63 0 0 1 96.9 160.9Z" fill="#d42a16"/>
    <path d="M113 100 L96.9 160.9 A63 63 0 0 1 68.7 144.8Z" fill="#f6910f"/>
    <path d="M113 100 L68.7 144.8 A63 63 0 0 1 52.3 116.7Z" fill="#1d9418"/>
    <path d="M113 100 L52.3 116.7 A63 63 0 0 1 113 37Z" fill="#930a9a"/>
    <g font-size="5" fill="#fff"><text x="153" y="90">45.8%</text><text x="66" y="66">29.2%</text><text x="62" y="123">8.3%</text><text x="80" y="143">8.3%</text><text x="106" y="151">8.3%</text></g>
    <g font-size="5"><circle cx="200" cy="35" r="2.5" fill="#2946c7"/><text x="205" y="37">Work</text><circle cx="200" cy="44.5" r="2.5" fill="#d42a16"/><text x="205" y="46.5">Eat</text><circle cx="200" cy="54" r="2.5" fill="#f6910f"/><text x="205" y="56">Commute</text><circle cx="200" cy="63.5" r="2.5" fill="#1d9418"/><text x="205" y="65.5">Watch TV</text><circle cx="200" cy="73" r="2.5" fill="#930a9a"/><text x="205" y="75">Sleep</text></g>
  </svg>
  <h2>Pie Chart</h2>
  <p>Lorem ipsum dolor sit amet, consectetur adipiscing elit. Phasellus quis magna turpis. Maecenas varius ornare convallis interdum magna ut augue rutrum luctus placerat gravida sodales..</p>
</article>

<article class="card" style="left:878px;top:441px">
  <svg class="chart" viewBox="0 0 268 180">
    <g stroke="#ddd" stroke-width=".5"><rect x="25" y="18" width="203" height="108" fill="none"/><line x1="76" y1="18" x2="76" y2="126"/><line x1="127" y1="18" x2="127" y2="126"/><line x1="177" y1="18" x2="177" y2="126"/><line x1="25" y1="45" x2="228" y2="45"/><line x1="25" y1="72" x2="228" y2="72"/><line x1="25" y1="99" x2="228" y2="99"/></g>
    <g font-size="4.5" fill="#444" text-anchor="end"><text x="20" y="20">6.0</text><text x="20" y="47">4.5</text><text x="20" y="74">3.0</text><text x="20" y="101">1.5</text><text x="20" y="128">0.0</text></g>
    <g font-size="4.5" fill="#444" text-anchor="middle"><text x="25" y="134">65</text><text x="76" y="134">70</text><text x="127" y="134">75</text><text x="177" y="134">80</text><text x="228" y="134">85</text><text x="127" y="148" font-style="italic">Life Expectancy</text></g>
    <g stroke="#fff" stroke-width=".6">
      <circle cx="55" cy="40" r="3" fill="#f6910f"/><circle cx="61" cy="98" r="7" fill="#d42a16"/><circle cx="101" cy="76" r="5" fill="#f6910f"/><circle cx="99" cy="95" r="5" fill="#f6910f"/>
      <circle cx="156" cy="89" r="10" fill="#2946c7"/><circle cx="177" cy="90" r="5" fill="#d42a16"/><circle cx="175" cy="101" r="5" fill="#d42a16"/><circle cx="183" cy="96" r="3" fill="#2946c7"/><circle cx="192" cy="73" r="2.5" fill="#f6910f"/>
    </g>
    <g font-size="4.5"><rect x="232" y="18" width="5" height="5" fill="#2946c7"/><text x="239" y="22">North Am</text><rect x="232" y="26" width="5" height="5" fill="#d42a16"/><text x="239" y="30">Europe</text><rect x="232" y="34" width="5" height="5" fill="#f6910f"/><text x="239" y="38">Middle E</text></g>
  </svg>
  <h2>Bubble Chart</h2>
  <p>Lorem ipsum dolor sit amet, consectetur adipiscing elit. Phasellus quis magna turpis. Maecenas varius ornare convallis interdum magna ut augue rutrum luctus placerat gravida sodales..</p>
</article>

<!-- Row 3 -->
<article class="card" style="left:319px;top:769px">
  <svg class="chart" viewBox="0 0 268 180">
    <rect x="184" y="12" width="70" height="3" fill="url(#tmgrad)"/>
    <defs><linearGradient id="tmgrad"><stop offset="0" stop-color="#d42a16"/><stop offset="1" stop-color="#6bbd5c"/></linearGradient></defs>
    <rect x="16" y="15" width="238" height="5" fill="#c8c8c8"/><text x="135" y="19" font-size="4" text-anchor="middle">Global</text>
    <g stroke="#fff" stroke-width="1">
      <rect x="16" y="20" width="79" height="152" fill="#c9d9c8"/>
      <rect x="95" y="20" width="73" height="152" fill="#dc9fa0"/>
      <rect x="168" y="20" width="86" height="74" fill="#ccd8cc"/>
      <rect x="168" y="94" width="86" height="78" fill="#b0dba6"/>
    </g>
    <g font-size="4" text-anchor="middle"><text x="55" y="98">Asia</text><text x="131" y="98">Europe</text><text x="211" y="58">America</text><text x="211" y="134">Africa</text></g>
  </svg>
  <h2>Treemaps</h2>
  <p>Lorem ipsum dolor sit amet, consectetur adipiscing elit. Phasellus quis magna turpis. Maecenas varius ornare convallis interdum magna ut augue rutrum luctus placerat gravida sodales..</p>
</article>

<article class="card" style="left:598px;top:769px">
  <svg class="chart" viewBox="0 0 268 180">
    <text x="36" y="19" font-size="5" font-weight="bold">Company Performance</text>
    <g stroke="#ddd" stroke-width=".5"><line x1="36" y1="28" x2="214" y2="28"/><line x1="36" y1="56" x2="214" y2="56"/><line x1="36" y1="84" x2="214" y2="84"/><line x1="36" y1="112" x2="214" y2="112"/></g>
    <path d="M36 140 L36 44 L95 31 L154 78 L214 46 L214 140Z" fill="#2946c7" fill-opacity=".35"/>
    <path d="M36 44 L95 31 L154 78 L214 46" fill="none" stroke="#2946c7" stroke-width=".8"/>
    <path d="M36 140 L36 101 L95 96 L154 36 L214 89 L214 140Z" fill="#d42a16" fill-opacity=".35"/>
    <path d="M36 101 L95 96 L154 36 L214 89" fill="none" stroke="#d42a16" stroke-width=".8"/>
    <line x1="36" y1="140" x2="214" y2="140" stroke="#333" stroke-width=".5"/>
    <g font-size="4.5" fill="#444" text-anchor="end"><text x="32" y="30">1,200</text><text x="32" y="58">900</text><text x="32" y="86">600</text><text x="32" y="114">300</text><text x="32" y="142">0</text></g>
    <g font-size="4.5" fill="#444" text-anchor="middle"><text x="36" y="147">2013</text><text x="95" y="147">2014</text><text x="154" y="147">2015</text><text x="214" y="147">2016</text><text x="125" y="161" font-style="italic">Year</text></g>
    <g font-size="4.5"><rect x="219" y="30" width="9" height="2" fill="#2946c7"/><text x="230" y="32">Sales</text><rect x="219" y="38" width="9" height="2" fill="#d42a16"/><text x="230" y="40">Expenses</text></g>
  </svg>
  <h2>Area Chart</h2>
  <p>Lorem ipsum dolor sit amet, consectetur adipiscing elit. Phasellus quis magna turpis. Maecenas varius ornare convallis interdum magna ut augue rutrum luctus placerat gravida sodales..</p>
</article>

<article class="card" style="left:878px;top:769px">
  <svg class="chart" viewBox="0 0 268 180">
    <g fill="#bdbdbd" fill-opacity=".85">
      <path d="M17 24 C130 24 130 20 249 20 L249 42 C130 42 130 44 17 44Z"/>
      <path d="M17 44 C130 44 130 50 249 50 L249 78 C130 78 130 72 17 72Z"/>
      <path d="M17 72 C130 72 130 108 249 108 L249 120 C130 120 130 86 17 86Z"/>
      <path d="M17 86 C130 86 130 42 249 42 L249 50 C130 50 130 94 17 94Z"/>
      <path d="M17 94 C130 94 130 78 249 78 L249 100 C130 100 130 114 17 114Z"/>
      <path d="M17 114 C130 114 130 120 249 120 L249 138 C130 138 130 138 17 138Z"/>
    </g>
    <rect x="14" y="24" width="4" height="62" fill="#3a6df0"/>
    <rect x="14" y="86" width="4" height="52" fill="#a33bbf"/>
    <rect x="249" y="20" width="4" height="22" fill="#d42a16"/>
    <rect x="249" y="42" width="4" height="66" fill="#f6b10f"/>
    <rect x="249" y="108" width="4" height="30" fill="#1d9418"/>
    <g font-size="4.5"><text x="21" y="57">A</text><text x="21" y="114">B</text><text x="244" y="33">X</text><text x="244" y="77">Y</text><text x="244" y="125">Z</text></g>
  </svg>
  <h2>Sankey Diagram</h2>
  <p>Lorem ipsum dolor sit amet, consectetur adipiscing elit. Phasellus quis magna turpis. Maecenas varius ornare convallis interdum magna ut augue rutrum luctus placerat gravida sodales..</p>
</article>
</body>
</html>
```